Business cards - ZELTO Roofing & Siding

We need simple business cards made up for our Roofing & Siding business based in Calgary Alberta.
The logo on one side of the card and potentially our slogan "Built with trust, verified by time".
The other side could have:
-A small logo
-Rep name:
-Rep cell phone:
-Rep email:
-Office phone: 403-688-2904
-Website: PrairieTopCrafters.com

We would like to incorporate the colours from our logo, especially the lite blue on the jpeg file. I have attached the ai file and jpeg file. We like the colours better on the jpeg file.

```html
<!DOCTYPE html>
<html lang="en">
<head>
<meta charset="utf-8">
<title>ZELTO Roofing &amp; Siding – Business Cards</title>
<link href="https://fonts.googleapis.com/css2?family=Montserrat:wght@400;500&family=Oswald:wght@600&display=swap" rel="stylesheet">
<style>
  :root {
    --brand-blue: #0468b8;
    --accent-blue: #1a86e0;
    --ink: #333a40;
    --paper: #ffffff;
    --backdrop: #e7e9ec;
  }
  * { box-sizing: border-box; margin: 0; padding: 0; }
  html, body { width: 1200px; height: 900px; overflow: hidden; }
  body {
    position: relative;
    background: var(--backdrop);
    font-family: "Montserrat", sans-serif;
  }
  .card {
    position: absolute;
    width: 560px;
    height: 320px;
    box-shadow: 0 6px 18px rgba(0, 0, 0, 0.18);
  }

  /* Front */
  .card-front {
    left: 60px;
    top: 90px;
    background: var(--brand-blue);
    color: var(--paper);
    display: flex;
    flex-direction: column;
    align-items: center;
    justify-content: center;
    gap: 6px;
  }
  .brand-name {
    font-weight: 500;
    color: var(--paper);
    text-align: center;
    line-height: 1.1;
  }
  .brand-name .brand-main { display: block; font-size: 64px; letter-spacing: 6px; }
  .brand-name .brand-sub { display: block; font-size: 20px; letter-spacing: 5px; text-transform: uppercase; }
  .brand-established {
    font-size: 13px;
    letter-spacing: 2px;
    margin-top: 6px;
  }

  /* Back */
  .card-back {
    left: 580px;
    top: 490px;
    background: var(--paper);
    display: flex;
    align-items: center;
    justify-content: center;
    gap: 22px;
    padding-left: 20px;
  }
  .rep {
    text-align: right;
  }
  .rep-name {
    font-family: "Oswald", sans-serif;
    font-weight: 600;
    font-size: 38px;
    line-height: 1;
    color: var(--accent-blue);
    text-transform: uppercase;
    letter-spacing: 0.5px;
  }
  .rep-title {
    font-size: 15px;
    color: var(--ink);
    letter-spacing: 1px;
    text-transform: uppercase;
    margin-top: 2px;
  }
  .divider {
    width: 1.5px;
    height: 96px;
    background: var(--accent-blue);
  }
  .contact-list {
    list-style: none;
    font-size: 14px;
    color: var(--ink);
    line-height: 1.45;
  }
  .contact-list li {
    display: flex;
    align-items: center;
    gap: 8px;
  }
  .contact-icon {
    width: 11px;
    height: 11px;
    flex: none;
    fill: none;
    stroke: var(--accent-blue);
    stroke-width: 1.6;
  }
</style>
</head>
<body>

<section class="card card-front" aria-label="Card front">
  <h1 class="brand-name">
    <span class="brand-main">ZELTO</span>
    <span class="brand-sub">Roofing &amp; Siding</span>
  </h1>
  <p class="brand-established">Est. 1991</p>
</section>

<section class="card card-back" aria-label="Card back">
  <div class="rep">
    <p class="rep-name">Daniel Moreau</p>
    <p class="rep-title">Director</p>
  </div>
  <div class="divider"></div>
  <ul class="contact-list">
    <li>
      <svg class="contact-icon" viewBox="0 0 12 12" aria-hidden="true"><path d="M2 1.5 L4 1.5 L5 4 L3.8 5 Q5 7.2 7 8.2 L8 7 L10.5 8 L10.5 10 Q6 11 2 5 Z"/></svg>
      403-688-2904
    </li>
    <li>
      <svg class="contact-icon" viewBox="0 0 12 12" aria-hidden="true"><rect x="3" y="1" width="6" height="10" rx="1"/><line x1="5.5" y1="9" x2="6.5" y2="9"/></svg>
      905-412-7390
    </li>
    <li>
      <svg class="contact-icon" viewBox="0 0 12 12" aria-hidden="true"><rect x="1" y="2.5" width="10" height="7"/><path d="M1 2.5 L6 6.5 L11 2.5"/></svg>
      zeltoroof@northmail.net
    </li>
    <li>
      <svg class="contact-icon" viewBox="0 0 12 12" aria-hidden="true"><circle cx="6" cy="6" r="5"/><ellipse cx="6" cy="6" rx="2.2" ry="5"/><line x1="1" y1="6" x2="11" y2="6"/></svg>
      PrairieTopCrafters.com
    </li>
  </ul>
</section>

</body>
</html>
```